Corvane Edge Supplies - Stone Tooling Company

We need a round design for a saw blade that cuts stone.

We provide the tools and equipment necessary to cut, shape, polish granite-marble-engineered stone for your home.

Think designs on a skateboard wheel. Urban-street designs. We like something along the lines of something similar to the wheels on larkhollowrolls.com, snowboard designs etc..

2 Colors. Background - Matte Black. Gold print on top.
No shading/gradient as this has to be solid colors black/gold.
We would like the following text imbedded somewhere-
"Approved by Tall Morris"
"Granite/Engineered Stone"

Must have logo thats in the file

Target Market(s)

granite countertop fabricators- current designs are boring- we want this to stand out.

Industry/Entity Type

It Company

Font styles to use
Sans Serif
Decorative

Requirements
Must have
• Check attached picture. Something similar except with our attached logo, black background, and gold print.
Nice to have
• urban, street, skate, surf, tattoo, style
Should not have
• shadowing, unless by dots and lines for silk screen printing.

```html
<!DOCTYPE html>
<html lang="en">
<head>
<meta charset="utf-8">
<title>Corvane Edge Supplies – Stone Saw Blade</title>
<link rel="stylesheet" href="https://fonts.googleapis.com/css2?family=Oswald:wght@700&display=swap">
<style>
  :root {
    --backdrop: #5b4c42;
    --steel: #cfd0d2;
    --steel-edge: #9fa1a4;
    --matte-black: #050505;
    --gold: #d9ae35;
  }
  html, body {
    margin: 0;
    padding: 0;
    width: 1200px;
    height: 1200px;
    overflow: hidden;
    background: var(--backdrop);
  }
  .blade {
    display: block;
    width: 1200px;
    height: 1200px;
  }
  .rim { fill: var(--steel); stroke: var(--steel-edge); stroke-width: 3; }
  .rim-slot { fill: var(--backdrop); }
  .rim-cut { stroke: var(--matte-black); stroke-width: 3; }
  .face { fill: var(--matte-black); }
  .mark-area { fill: var(--gold); }
  .arbor-gap { fill: var(--matte-black); }
  .arbor-ring { fill: var(--steel); stroke: var(--steel-edge); stroke-width: 3; }
  .arbor-hole { fill: var(--backdrop); }
  .ring-label {
    font-family: "Oswald", sans-serif;
    font-weight: 700;
    font-size: 42px;
    letter-spacing: 1px;
    fill: var(--gold);
  }
  .ring-arrow { fill: none; stroke: var(--gold); stroke-width: 18; }
  .arrow-head { fill: var(--gold); }
  .brand-name {
    font-family: "Oswald", sans-serif;
    font-weight: 700;
    font-size: 84px;
    fill: var(--gold);
  }
  .endorsement {
    font-family: "Oswald", sans-serif;
    font-weight: 700;
    font-size: 26px;
    letter-spacing: 0.5px;
    fill: var(--gold);
  }
</style>
</head>
<body>
<svg class="blade" viewBox="0 0 1200 1200" xmlns="http://www.w3.org/2000/svg" role="img" aria-label="Corvane Edge Supplies stone saw blade, approved by Tall Morris, for granite and engineered stone">
  <defs>
    <g id="slot">
      <rect class="rim-slot" x="593" y="38" width="14" height="52"/>
      <line class="rim-cut" x1="600" y1="90" x2="600" y2="118"/>
    </g>
    <path id="label-track" d="M 180 600 A 420 420 0 1 1 1020 600 A 420 420 0 1 1 180 600"/>
    <marker id="arrow-tip" viewBox="0 0 10 10" refX="3" refY="5" markerWidth="3.2" markerHeight="3.2" orient="auto">
      <path class="arrow-head" d="M0 0 L10 5 L0 10 Z"/>
    </marker>
    <g id="label-segment">
      <text class="ring-label"><textPath href="#label-track" startOffset="8">GRANITE / ENGINEERED STONE</textPath></text>
      <path class="ring-arrow" d="M 552 170 A 432 432 0 0 1 790 210" marker-end="url(#arrow-tip)"/>
    </g>
    <g id="brand-block">
      <text class="brand-name" x="600" y="338" text-anchor="middle">Corvane</text>
      <text class="endorsement" x="600" y="377" text-anchor="middle">APPROVED BY TALL MORRIS</text>
    </g>
  </defs>

  <circle class="rim" cx="600" cy="600" r="560"/>
  <g class="rim-slots">
    <use href="#slot" transform="rotate(0 600 600)"/>
    <use href="#slot" transform="rotate(9 600 600)"/>
    <use href="#slot" transform="rotate(18 600 600)"/>
    <use href="#slot" transform="rotate(27 600 600)"/>
    <use href="#slot" transform="rotate(36 600 600)"/>
    <use href="#slot" transform="rotate(45 600 600)"/>
    <use href="#slot" transform="rotate(54 600 600)"/>
    <use href="#slot" transform="rotate(63 600 600)"/>
    <use href="#slot" transform="rotate(72 600 600)"/>
    <use href="#slot" transform="rotate(81 600 600)"/>
    <use href="#slot" transform="rotate(90 600 600)"/>
    <use href="#slot" transform="rotate(99 600 600)"/>
    <use href="#slot" transform="rotate(108 600 600)"/>
    <use href="#slot" transform="rotate(117 600 600)"/>
    <use href="#slot" transform="rotate(126 600 600)"/>
    <use href="#slot" transform="rotate(135 600 600)"/>
    <use href="#slot" transform="rotate(144 600 600)"/>
    <use href="#slot" transform="rotate(153 600 600)"/>
    <use href="#slot" transform="rotate(162 600 600)"/>
    <use href="#slot" transform="rotate(171 600 600)"/>
    <use href="#slot" transform="rotate(180 600 600)"/>
    <use href="#slot" transform="rotate(189 600 600)"/>
    <use href="#slot" transform="rotate(198 600 600)"/>
    <use href="#slot" transform="rotate(207 600 600)"/>
    <use href="#slot" transform="rotate(216 600 600)"/>
    <use href="#slot" transform="rotate(225 600 600)"/>
    <use href="#slot" transform="rotate(234 600 600)"/>
    <use href="#slot" transform="rotate(243 600 600)"/>
    <use href="#slot" transform="rotate(252 600 600)"/>
    <use href="#slot" transform="rotate(261 600 600)"/>
    <use href="#slot" transform="rotate(270 600 600)"/>
    <use href="#slot" transform="rotate(279 600 600)"/>
    <use href="#slot" transform="rotate(288 600 600)"/>
    <use href="#slot" transform="rotate(297 600 600)"/>
    <use href="#slot" transform="rotate(306 600 600)"/>
    <use href="#slot" transform="rotate(315 600 600)"/>
    <use href="#slot" transform="rotate(324 600 600)"/>
    <use href="#slot" transform="rotate(333 600 600)"/>
    <use href="#slot" transform="rotate(342 600 600)"/>
    <use href="#slot" transform="rotate(351 600 600)"/>
  </g>

  <circle class="face" cx="600" cy="600" r="488"/>

  <g class="ring-labels">
    <use href="#label-segment" transform="rotate(12 600 600)"/>
    <use href="#label-segment" transform="rotate(132 600 600)"/>
    <use href="#label-segment" transform="rotate(252 600 600)"/>
  </g>

  <g class="brand-blocks">
    <use href="#brand-block"/>
    <use href="#brand-block" transform="rotate(120 600 600)"/>
    <use href="#brand-block" transform="rotate(240 600 600)"/>
  </g>

  <circle class="mark-area" cx="600" cy="600" r="180" role="img" aria-label="Corvane Edge Supplies logo mark in gold at the blade centre"/>
  <circle class="arbor-gap" cx="600" cy="600" r="88"/>
  <circle class="arbor-ring" cx="600" cy="600" r="74"/>
  <circle class="arbor-hole" cx="600" cy="600" r="62"/>
</svg>
</body>
</html>
```